Geschäftspapiere für Termin Startup
Zielgruppe
Wir sind ein Startup, das über die Seite Planorix.de (derzeit noch in der Beta-Phase)zukünftig folgenden Service anbietet: Unternehmer können sehr flexibel (selbst) gestaltete Terminformulare erstellen und auf Ihrer Website einbinden. Kunden können dann diese Termine buchen und bekommen dann Erinnerungs-Mails und SMS.
Zielgruppe: Dienstleister wie Fotografen, Friseure, Versicherungsvertreter, Masseure, Restaurants, Arztpraxen. Also alle, die darauf angewiesen sind, dass vereinbarte Termine eingehalten werden und die die Terminvereinbarung vereinfachen wollen. Also weniger per Telefon, mehr über die eigene Website.
Dateien bitte beachten für die Ansicht des Look & Feels:
https://ablage.beispielwolke.de/open?id=7QmrtHkWz2LpA94bNc3sVyTeOx8dGJuR_
Bonus-Aktion: Wir zahlen pauschal jeweils 30,00 Euro an die Designer auf den Plätzen 2 bis 4 für die geleistete Arbeit. Nur einer kann gewinnen und den Zuschlag bekommen. Aber so möchten wir gerne die Arbeit dennoch honorieren.
Aufgabenstellung
Wir benötigen ein modernes Briefpapier-Layout passend zu unserem CD.
Gerne darf/soll der ORBO (siehe Maskottchen in https://ablage.beispielwolke.de/open?id=5PwqNsYt8BaLmr2Hc7xkDuQOEPfjWzVbn )darauf erscheinen.
Maskottchen ORBO gibt es in mehreren Varianten. Siehe https://ablage.beispielwolke.de/ordner/8TrnWqLeHd5XcmZ3sJ4yPvBkGfQaNuRox?teilen=ja
Auch als Variante, das Maskottchen ORBO gegen das Logo gelehnt ist, kann genutzt werden: https://ablage.beispielwolke.de/open?id=3MuxBgTpW7RkaNj6yVqLeDsHcZoPfGtYi
Das Thema 'Terminvereinbarung' soll sofort erfasst werden mittels des Layouts bzw. der grafischen Elemente.
Auch die Branchen-Icons ( https://ablage.beispielwolke.de/ordner/6HpvRtNmQ2WkzLx8yEcBaJdFsUoGiTbeq?teilen=ja ) dürfen verwendet werden.

```html
<!DOCTYPE html>
<html lang="de">
<head>
<meta charset="utf-8">
<title>Planorix Geschäftsausstattung</title>
<link rel="stylesheet" href="https://fonts.googleapis.com/css2?family=Titillium+Web:wght@300;400;600;700&display=swap">
<style>
:root{
  --green:#7ab829;
  --ink:#2b2b2b;
  --text:#3c3c3c;
  --muted:#6d6e71;
  --band:#5f6366;
  --sheet:#f8f8f9;
  --panel-top:#e4e5e7;
  --panel-bottom:#d9dadc;
  --stage:#a9aaab;
  --art-a:#cfd1d3;
  --art-b:#9cc458;
}
*{margin:0;padding:0;box-sizing:border-box}
html,body{width:1200px;height:2186px;overflow:hidden;background:#fff}
body{position:relative;font-family:"Titillium Web",sans-serif;color:var(--text)}

.hero{position:absolute;left:0;top:0;width:1200px;height:1092px;background:#fff}
.stage{position:absolute;left:0;top:1092px;width:1200px;height:1094px;background:var(--stage)}

.letter{position:absolute;width:726px;height:1025px;background:var(--sheet);box-shadow:0 6px 18px rgba(0,0,0,.18);overflow:hidden}
.letter--hero{left:231px;top:30px}
.letter--small{left:397px;top:50px;transform:scale(.6143);transform-origin:0 0;box-shadow:none}

.letter__band{position:absolute;left:0;top:0;width:507px;height:12px;background:var(--band)}
.letter__sidebar{position:absolute;left:507px;top:96px;width:219px;bottom:0;background:linear-gradient(180deg,var(--panel-top),var(--panel-bottom))}

.brand{position:absolute;display:flex;align-items:center;gap:6px}
.brand__mark{width:20px;height:20px;background:var(--muted)}
.brand__name{font-weight:600;color:var(--muted);line-height:1}
.letter .brand{left:530px;top:28px}
.letter .brand__name{font-size:34px}
.brand__tag{position:absolute;font-size:9px;color:var(--muted);white-space:nowrap}
.letter .brand__tag{right:20px;top:60px}
.brand__tag b{font-weight:400;color:var(--green)}

.side{position:absolute;font-size:10px;line-height:14px;font-weight:300;color:var(--muted)}
.side--company{left:529px;top:108px;font-weight:600;color:var(--text)}
.side--address{left:529px;top:135px}
.contact{position:absolute;left:529px;width:155px;display:flex;justify-content:space-between;align-items:center;font-size:10px;font-weight:300;color:var(--muted)}
.contact svg{width:16px;height:16px;fill:var(--muted)}
.side--tax{left:529px;top:357px}
.side--bank{left:529px;top:401px}
.bank-table{position:absolute;left:529px;top:445px;width:155px;font-size:10px;line-height:14.5px;font-weight:300;color:var(--muted)}
.bank-table div{display:flex;justify-content:space-between}

.mascot-art{position:absolute;left:497px;top:680px;width:229px;height:315px;border-radius:115px 0 0 0;background:radial-gradient(circle at 62% 45%,var(--art-b) 0 22%,var(--art-a) 60%,rgba(217,218,220,0) 78%)}
.page-no{position:absolute;right:23px;top:996px;font-size:11px;color:var(--ink)}

.sender{position:absolute;left:69px;top:148px;font-size:9px;font-weight:300;color:var(--muted)}
.sender b{font-weight:600;color:var(--green)}
.recipient{position:absolute;left:70px;top:170px;font-size:13px;line-height:16px;color:var(--ink)}
.fold{position:absolute;left:0;width:26px;height:1px;background:#b9bbbd}

.body{position:absolute;left:92px;top:307px;width:342px;font-size:11px;line-height:17px;color:var(--ink)}
.body h1{font-size:10.5px;font-weight:700;margin-bottom:34px}
.body p{margin-bottom:17px}
.body .gap{margin-bottom:34px}

.card{position:absolute;background:var(--sheet);overflow:hidden}
.card--front{left:241px;top:732px;width:179px;height:112px}
.card--front .brand{left:9px;top:12px;gap:3px}
.card--front .brand__mark{width:14px;height:14px}
.card--front .brand__name{font-size:21px}
.card--front .brand__tag{left:64px;top:34px;font-size:5.5px}
.card__art{position:absolute;right:6px;top:34px;width:56px;height:64px;border-radius:50%;background:radial-gradient(circle,var(--art-b) 0 35%,rgba(207,209,211,0) 75%)}
.card__band{position:absolute;left:0;bottom:0;width:100%;height:9px;background:var(--band)}

.card--back{left:241px;top:874px;width:183px;height:115px}
.card--back .panel{position:absolute;left:107px;top:0;right:0;bottom:0;background:linear-gradient(180deg,var(--panel-top),var(--panel-bottom))}
.card--back .person{position:absolute;left:14px;top:44px;font-size:5.5px;line-height:9px;color:var(--ink)}
.card--back .person span{color:var(--green)}
.card--back .info{position:absolute;left:111px;top:44px;width:68px;font-size:4.5px;line-height:7px;color:var(--muted)}
.card--back .info strong{color:var(--ink);font-weight:600}
.card--back .row{display:flex;justify-content:space-between}

.envelope{position:absolute;left:491px;top:748px;width:495px;height:235px;background:var(--sheet);overflow:hidden}
.envelope__window{position:absolute;left:43px;top:108px;width:184px;height:95px;border-radius:8px;background:#e2e3e4;border:1px solid #cfd0d2}
.envelope__art{position:absolute;left:340px;top:90px;width:150px;height:133px;border-radius:75px 75px 0 0;background:radial-gradient(circle at 55% 55%,var(--art-b) 0 22%,var(--art-a) 58%,rgba(217,218,220,0) 76%)}
.envelope__band{position:absolute;left:0;bottom:0;width:100%;height:12px;background:var(--band)}
</style>
</head>
<body>

<section class="hero">
  <article class="letter letter--hero">
    <div class="letter__band"></div>
    <div class="letter__sidebar"></div>
    <div class="brand"><span class="brand__mark"></span><span class="brand__name">Planorix</span></div>
    <div class="brand__tag">Tool by <b>datumfix-werk.de</b></div>

    <div class="side side--company">Planorix GmbH</div>
    <div class="side side--address">Lindenweg 14<br>70519 Musterau</div>
    <div class="contact" style="top:187px"><svg viewBox="0 0 24 24"><path d="M6.6 10.8a15 15 0 0 0 6.6 6.6l2.2-2.2c.3-.3.7-.4 1-.2 1.1.4 2.3.6 3.6.6.6 0 1 .4 1 1V20c0 .6-.4 1-1 1A17 17 0 0 1 3 4c0-.6.4-1 1-1h3.5c.6 0 1 .4 1 1 0 1.3.2 2.5.6 3.6.1.3 0 .7-.2 1z"/></svg><span>+42 811 704 190</span></div>
    <div class="contact" style="top:214px"><svg viewBox="0 0 24 24"><path d="M7 3h10v5H7zM4 9h16a2 2 0 0 1 2 2v6h-4v4H6v-4H2v-6a2 2 0 0 1 2-2zm4 7v3h8v-3z"/></svg><span>+42 2633 482 20 25</span></div>
    <div class="contact" style="top:241px"><svg viewBox="0 0 24 24"><path d="M12 2a10 10 0 1 0 5 18.7l-1-1.7A8 8 0 1 1 20 12v1a2 2 0 0 1-4 0V8h-2v1a5 5 0 1 0 .7 6.2A4 4 0 0 0 22 13v-1A10 10 0 0 0 12 2zm0 13a3 3 0 1 1 0-6 3 3 0 0 1 0 6z"/></svg><span>office@planorix.de</span></div>

    <div class="side side--tax">Steuer Nr.: 27481/30592<br>UID-Nr.: DE 294817365</div>
    <div class="side side--bank">Bankverbindung:<br>Beispielbank Süd</div>
    <div class="bank-table">
      <div><span>BLZ:</span><span>371 208 55</span></div>
      <div><span>Konto-Nr.:</span><span>618 29 07</span></div>
      <div><span>IBAN:</span><span>DE71 3712 0855 6182 90</span></div>
    </div>

    <div class="mascot-art" role="img" aria-label="Maskottchen mit grünem Zaubererhut und Terminkalender vor einem großen Zahnrad"></div>
    <div class="page-no">1 von 1</div>

    <div class="sender"><b>Planorix</b> &nbsp;|&nbsp; Lindenweg 14 &nbsp;|&nbsp; 70519 Musterau</div>
    <div class="recipient">Herr Kellner<br>Am Feldrain 9<br>80347 Wiesental</div>

    <div class="fold" style="top:347px"></div>
    <div class="fold" style="top:513px"></div>
    <div class="fold" style="top:698px"></div>

    <div class="body">
      <h1>Auftrag XY 303983</h1>
      <p class="gap">Sehr geehrter Herr Kellner,</p>
      <p>dicipic tene nos dolupti cus ium fugitio vendam,</p>
      <p>corpore, optatum, od quissita delecatis poribus et aut porehenis audam non pos eos eri dolessincto dolluptiunda volecup tatem. Ut duntiandest hillabor sequae prate omnientio cuptam untur?<br>Us et, as re iliquis unti omnis denitec tatiae sedi in et fugitiis et ipsandun-tem. Picipsae vellatur?</p>
      <p class="gap">Aperem landant ra conseration rerum faccus solentem hilis et, sundia velit aut que accabor aut et ad quam quiatus, ut dem illorepero tem esti as et volore acerum dolupta quidel eum nuscil estibus nobit, quos et quo quiae volorite ex estrundel molestrunt fugia quiatur magnis volore et earibus, nonsecto idit offic te culliquodi beror sim voluptat aut asperepu-dae lam quiam facea pratis eatium eos sitate et aditiatianit odia aliqui cullore et re pa sunt aditaturit eos min consequ odipsam entectiissi officid mint, site mi, con remo bla sincillibus que excessendae lacernatia volut fugiaecatur asped ma volo et et alit eate et ipsunt pre nullis ut volut dusam, voluptassi atem lant, cus molores tiatiae.</p>
      <p>Mit freundlichen Grüßen,</p>
    </div>
  </article>
</section>

<section class="stage">
  <article class="letter letter--small">
    <div class="letter__band"></div>
    <div class="letter__sidebar"></div>
    <div class="brand"><span class="brand__mark"></span><span class="brand__name">Planorix</span></div>
    <div class="brand__tag">Tool by <b>datumfix-werk.de</b></div>
    <div class="side side--company">Planorix GmbH</div>
    <div class="side side--address">Lindenweg 14<br>70519 Musterau</div>
    <div class="contact" style="top:187px"><svg viewBox="0 0 24 24"><path d="M6.6 10.8a15 15 0 0 0 6.6 6.6l2.2-2.2c.3-.3.7-.4 1-.2 1.1.4 2.3.6 3.6.6.6 0 1 .4 1 1V20c0 .6-.4 1-1 1A17 17 0 0 1 3 4c0-.6.4-1 1-1h3.5c.6 0 1 .4 1 1 0 1.3.2 2.5.6 3.6.1.3 0 .7-.2 1z"/></svg><span>+42 811 704 190</span></div>
    <div class="contact" style="top:214px"><svg viewBox="0 0 24 24"><path d="M7 3h10v5H7zM4 9h16a2 2 0 0 1 2 2v6h-4v4H6v-4H2v-6a2 2 0 0 1 2-2zm4 7v3h8v-3z"/></svg><span>+42 2633 482 20 25</span></div>
    <div class="contact" style="top:241px"><svg viewBox="0 0 24 24"><path d="M12 2a10 10 0 1 0 5 18.7l-1-1.7A8 8 0 1 1 20 12v1a2 2 0 0 1-4 0V8h-2v1a5 5 0 1 0 .7 6.2A4 4 0 0 0 22 13v-1A10 10 0 0 0 12 2zm0 13a3 3 0 1 1 0-6 3 3 0 0 1 0 6z"/></svg><span>office@planorix.de</span></div>
    <div class="side side--tax">Steuer Nr.: 27481/30592<br>UID-Nr.: DE 294817365</div>
    <div class="side side--bank">Bankverbindung:<br>Beispielbank Süd</div>
    <div class="bank-table">
      <div><span>BLZ:</span><span>371 208 55</span></div>
      <div><span>Konto-Nr.:</span><span>618 29 07</span></div>
      <div><span>IBAN:</span><span>DE71 3712 0855 6182 90</span></div>
    </div>
    <div class="mascot-art" role="img" aria-label="Maskottchen mit grünem Zaubererhut und Terminkalender vor einem großen Zahnrad"></div>
    <div class="page-no">1 von 1</div>
    <div class="sender"><b>Planorix</b> &nbsp;|&nbsp; Lindenweg 14 &nbsp;|&nbsp; 70519 Musterau</div>
    <div class="recipient">Herr Kellner<br>Am Feldrain 9<br>80347 Wiesental</div>
    <div class="fold" style="top:347px"></div>
    <div class="fold" style="top:513px"></div>
    <div class="fold" style="top:698px"></div>
    <div class="body">
      <h1>Auftrag XY 303983</h1>
      <p class="gap">Sehr geehrter Herr Kellner,</p>
      <p>dicipic tene nos dolupti cus ium fugitio vendam,</p>
      <p>corpore, optatum, od quissita delecatis poribus et aut porehenis audam non pos eos eri dolessincto dolluptiunda volecup tatem. Ut duntiandest hillabor sequae prate omnientio cuptam untur?<br>Us et, as re iliquis unti omnis denitec tatiae sedi in et fugitiis et ipsandun-tem. Picipsae vellatur?</p>
      <p class="gap">Aperem landant ra conseration rerum faccus solentem hilis et, sundia velit aut que accabor aut et ad quam quiatus, ut dem illorepero tem esti as et volore acerum dolupta quidel eum nuscil estibus nobit, quos et quo quiae volorite ex estrundel molestrunt fugia quiatur magnis volore et earibus, nonsecto idit offic te culliquodi beror sim voluptat aut asperepu-dae lam quiam facea pratis eatium eos sitate et aditiatianit odia aliqui cullore et re pa sunt aditaturit eos min consequ odipsam entectiissi officid mint, site mi, con remo bla sincillibus que excessendae lacernatia volut fugiaecatur asped ma volo et et alit eate et ipsunt pre nullis ut volut dusam, voluptassi atem lant, cus molores tiatiae.</p>
      <p>Mit freundlichen Grüßen,</p>
    </div>
  </article>

  <article class="card card--front">
    <div class="brand"><span class="brand__mark"></span><span class="brand__name">Planorix</span></div>
    <div class="brand__tag">Tool by <b>datumfix-werk.de</b></div>
    <div class="card__art" role="img" aria-label="Maskottchen mit Terminkalender"></div>
    <div class="card__band"></div>
  </article>

  <article class="card card--back">
    <div class="panel"></div>
    <div class="person">Jonas Reiter<br><span>Geschäftsführer</span></div>
    <div class="info">
      <strong>Planorix GmbH</strong><br><br>
      Lindenweg 14<br>70519 Musterau<br>
      <div class="row"><span>✆</span><span>+42 811 704 190</span></div>
      <div class="row"><span>▣</span><span>+42 2633 482 20 25</span></div>
      <div class="row"><span>@</span><span>office@planorix.de</span></div>
    </div>
  </article>

  <article class="envelope">
    <div class="envelope__window"></div>
    <div class="envelope__art" role="img" aria-label="Maskottchen mit Terminkalender vor einem Zahnrad"></div>
    <div class="envelope__band"></div>
  </article>
</section>

</body>
</html>
```